Marlow Crest Group (Real Estate and Investment)

A high end, clean design.
We are a real estate company with sales, asset management and investment divisions. We want to use a black and white scheme which is really high end feel. The back of the card can just be the logo (black background with the white writing) as we will probably emboss this when we print)

Target Market(s)

High level investors, high end houses for sale

Industry/Entity Type

Business

Contact Information for Business Card

Name, position, phone number and email address
Glen Varley, Managing Director, 0437259064 and glen@marlowcrest-example.com.au

Requirements
Must have
• Back of the card to be the black background with the white writing (as per the attached images). Would like the capacity to emboss the writing and logo

```html
<!DOCTYPE html>
<html lang="en">
<head>
<meta charset="utf-8">
<title>Marlow Crest Group — Business Card</title>
<link href="https://fonts.googleapis.com/css2?family=Lato:wght@400;700&display=swap" rel="stylesheet">
<style>
  :root {
    --backdrop: #1b1c1f;
    --card: #050505;
    --accent: #ffffff;
    --ink: #d6d6d6;
    --rule: #4a4a4a;
  }
  * { margin: 0; padding: 0; box-sizing: border-box; }
  html, body {
    width: 1200px;
    height: 900px;
    overflow: hidden;
    background: var(--backdrop);
    font-family: "Lato", Arial, sans-serif;
  }
  .canvas {
    width: 1200px;
    height: 900px;
    display: flex;
    align-items: center;
    justify-content: center;
    gap: 40px;
  }
  .card {
    width: 540px;
    height: 309px;
    background: var(--card);
    position: relative;
    box-shadow: 0 10px 30px rgba(0,0,0,0.45);
  }
  .wordmark {
    color: var(--accent);
    font-weight: 700;
    line-height: 1.1;
    display: flex;
    align-items: center;
    gap: 10px;
  }
  .wordmark__square {
    width: 12px;
    height: 12px;
    background: var(--accent);
    flex: none;
  }
  /* Front */
  .card--front .wordmark {
    position: absolute;
    left: 40px;
    top: 104px;
    font-size: 22px;
    width: 190px;
  }
  .card--front .divider {
    position: absolute;
    left: 238px;
    top: 62px;
    width: 1px;
    height: 185px;
    background: var(--rule);
  }
  .contact {
    position: absolute;
    left: 262px;
    top: 92px;
    color: var(--ink);
  }
  .contact__name {
    color: var(--accent);
    font-weight: 700;
    font-size: 24px;
    letter-spacing: 0.2px;
    white-space: nowrap;
  }
  .contact__title {
    font-size: 13px;
    margin-top: 2px;
    margin-bottom: 18px;
    white-space: nowrap;
  }
  .contact__row {
    display: flex;
    align-items: center;
    gap: 10px;
    font-size: 14px;
    margin-bottom: 12px;
    white-space: nowrap;
  }
  .contact__icon {
    width: 20px;
    height: 20px;
    flex: none;
  }
  /* Back */
  .card--back {
    display: flex;
    align-items: center;
    justify-content: center;
  }
  .card--back .wordmark {
    font-size: 30px;
  }
</style>
</head>
<body>
<main class="canvas">
  <section class="card card--front" aria-label="Card front">
    <div class="wordmark">
      <span class="wordmark__square"></span>
      <span>Marlow Crest Group</span>
    </div>
    <div class="divider"></div>
    <div class="contact">
      <div class="contact__name">Glen Varley</div>
      <div class="contact__title">Managing Director</div>
      <div class="contact__row">
        <svg class="contact__icon" viewBox="0 0 20 20" aria-hidden="true">
          <rect width="20" height="20" rx="3" fill="var(--accent)"/>
          <path d="M6.5 4.5 L8.5 4.5 L9.3 7.6 L7.9 8.6 C8.6 10.2 9.8 11.4 11.4 12.1 L12.4 10.7 L15.5 11.5 L15.5 13.5 C15.5 14.6 14.6 15.5 13.5 15.5 C8.8 15.2 4.8 11.2 4.5 6.5 C4.5 5.4 5.4 4.5 6.5 4.5 Z" fill="var(--card)"/>
        </svg>
        <span>0437259064</span>
      </div>
      <div class="contact__row">
        <svg class="contact__icon" viewBox="0 0 20 20" aria-hidden="true">
          <rect x="1" y="4" width="18" height="12" fill="var(--accent)"/>
          <path d="M1 4 L10 11 L19 4" fill="none" stroke="var(--card)" stroke-width="1.4"/>
        </svg>
        <span>glen@marlowcrest-example.com.au</span>
      </div>
    </div>
  </section>

  <section class="card card--back" aria-label="Card back">
    <div class="wordmark">
      <span class="wordmark__square"></span>
      <span>Marlow Crest Group</span>
    </div>
  </section>
</main>
</body>
</html>
```